Landing Page and Logo for Auto-Blogging Platform

I created a platform that allows users to start a blog for their business, hobby, charity, etc. I need a landing page where users can learn about the platform, benefits of consistent blogging, SEO value, plans/pricing, etc. The landing page needs to have multiple call to action buttons encouraging the visitor to register/sign up for a free trial.

In addition to the landing page, I need a page for users to establish the settings for their blog. This page should be a fairly simple form, intended for the user to enter a few details to set up their blog:
1. Name of Blog
2. Up to 10 topics and/or keywords the blog should focus on
3. Theme: Color-scheme and logo upload for blog.

I have attached the specifications of the platform's functionality so you can better understand how it works, plans/pricing, etc.

I also need a logo for the business. The name of the platform is PennaWave.

Target Market(s)

Website owners, bloggers, business owners

Industry/Entity Type

Technology, Internet, web design

Coding

Coded - Design and coding required

Number of Pages Required

2 page

Colors
0054AA
0677BA
7BADD7
CADEEF
E8F1F8
0094D4
00A9DD
6FCCEA
C7EBF8
E9F6FB

Requirements
Must have
• Eye-catching design but fairly light on content (keep it simple and brief.)
Nice to have
• Eye-catching yet simple design, clean and easy to understand what we are offering.
Should not have
• Too much “wordy” and confusing content.

```html
<!DOCTYPE html>
<html lang="en">
<head>
<meta charset="UTF-8">
<title>PennaWave – Automate Your Blog Posting with AI</title>
<link href="https://fonts.googleapis.com/css2?family=Poppins:wght@300;400;500;600;700;800&family=Open+Sans:wght@400&display=swap" rel="stylesheet">
<style>
:root{
  --navy:#0054AA;
  --blue:#0677BA;
  --sky:#0094D4;
  --cyan:#00A9DD;
  --aqua:#6FCCEA;
  --ice:#C7EBF8;
  --mist:#E9F6FB;
  --band:#D6EEF9;
  --ink:#1d1d1f;
  --grey:#6b6f76;
  --dark:#231f20;
  --gold:#F5A623;
  --white:#fff;
  --grad:linear-gradient(90deg,var(--navy),var(--aqua));
  --shadow:0 14px 40px rgba(20,60,110,.10);
}
*{box-sizing:border-box;margin:0;padding:0}
html,body{width:1200px;height:3980px;overflow:hidden}
body{position:relative;background:var(--white);font-family:"Poppins",sans-serif;color:var(--ink)}
.abs{position:absolute}
.brand{font-weight:600;color:var(--blue);font-family:"Poppins",sans-serif}
.btn{position:absolute;display:flex;align-items:center;justify-content:space-between;height:40px;border-radius:22px;background:var(--grad);color:#fff;font-size:13px;font-weight:600;padding:0 5px 0 22px}
.btn .arr{width:32px;height:32px;border-radius:50%;background:var(--navy);display:flex;align-items:center;justify-content:center;border:2px solid rgba(255,255,255,.7)}
.btn.light{background:#fff;color:var(--ink)}
.pill-link{color:var(--ink)}
.eyebrow{position:absolute;left:0;width:1200px;text-align:center;color:var(--blue);font-size:13px;font-weight:600}
.h2{position:absolute;left:0;width:1200px;text-align:center;font-size:36px;font-weight:600}
.ph{position:absolute}

/* nav */
.nav a{position:absolute;top:26px;font-size:12px;color:var(--ink);text-decoration:none}

/* step cards */
.step-card{position:absolute;top:814px;width:244px;height:213px;background:#fff;border-radius:12px;box-shadow:var(--shadow);text-align:center;padding-top:18px}
.step-card .ico{width:62px;height:56px;margin:0 auto 10px;border-radius:10px}
.step-card h3{font-size:17px;font-weight:600;margin-bottom:8px}
.step-card p{font-size:11.5px;line-height:1.7;color:var(--grey);padding:0 22px}
.step-card .go{position:absolute;left:103px;bottom:-18px;width:38px;height:38px;border-radius:50%;background:var(--grad);display:flex;align-items:center;justify-content:center}

/* why */
.bullets li{list-style:none;font-size:12px;font-weight:500;color:#444;margin-bottom:12px;position:relative;padding-left:18px}
.bullets li::before{content:"";position:absolute;left:0;top:5px;width:8px;height:8px;border-radius:50%;background:var(--navy)}

/* setup steps */
.setup-band{position:absolute;left:0;top:1714px;width:1200px;height:533px;background:var(--band)}
.bubble{position:absolute;width:124px;height:124px;border-radius:50%;background:#fff;box-shadow:0 10px 26px rgba(0,60,120,.15);display:flex;align-items:center;justify-content:center}
.bubble .ico{width:60px;height:54px;border-radius:10px}
.setup-txt h4{font-size:17px;font-weight:600;margin-bottom:6px}
.setup-txt p{font-size:11.5px;line-height:1.7;color:var(--grey)}

/* pricing */
.plan{position:absolute;top:2450px;height:473px;background:#fff;border-radius:6px;box-shadow:var(--shadow);text-align:center}
.plan h3{font-size:21px;font-weight:600;margin-top:44px}
.plan .rule{width:178px;height:1px;background:#bbb;margin:0 auto}
.plan .sm{font-size:13px;color:#444}
.plan .big{font-size:22px;font-weight:400;margin:22px 0 24px}
.plan .price{font-size:25px;font-weight:500;margin-top:34px}
.plan .cta{width:144px;height:42px;border-radius:22px;margin:42px auto 0;background:var(--grad);color:#fff;font-size:14px;font-weight:600;display:flex;align-items:center;justify-content:center}
.plan.featured{background:linear-gradient(180deg,#6FCCEA 0%,#0094D4 45%,#0054AA 100%);color:#fff}
.plan.featured .rule{background:rgba(255,255,255,.6)}
.plan.featured .sm{color:#fff}
.plan.featured .cta{background:#fff;color:var(--ink)}

/* testimonials */
.quote-card{position:absolute;top:3111px;width:484px;height:252px;background:#fff;border-radius:18px;box-shadow:var(--shadow)}
.stars{color:var(--gold);font-size:15px;letter-spacing:1px}
.quote-card p{font-size:12px;line-height:1.35;color:var(--grey);width:232px;margin-top:8px}
.quote-card .who{position:absolute;left:34px;top:184px;font-size:13px;font-weight:600;color:#555}
.quote-card .line{position:absolute;left:34px;top:165px;width:160px;height:1px;background:#e4e4e4}
.quote-card .photo{position:absolute;left:284px;top:54px;width:164px;height:164px;border-radius:50%;border:4px solid var(--blue)}
.quote-card .qmark{position:absolute;left:387px;top:38px;width:62px;height:62px;border-radius:50%;background:var(--blue);border:5px solid #fff;color:#fff;font-size:40px;font-weight:700;text-align:center;line-height:64px}
.slider-arrow{position:absolute;top:3023px;width:46px;height:46px;border-radius:50%;border:2px solid #555;display:flex;align-items:center;justify-content:center}

/* footer */
.footer{position:absolute;left:0;top:3659px;width:1200px;height:321px;background:var(--dark)}
.cta-banner{position:absolute;left:199px;top:3540px;width:801px;height:227px;border-radius:114px;background:linear-gradient(100deg,var(--navy) 0%,var(--sky) 55%,var(--aqua) 100%);text-align:center;color:#fff}
.foot-links a{position:absolute;top:3847px;font-size:14px;font-weight:500;color:#fff;text-decoration:none}
</style>
</head>
<body>

<!-- Navigation -->
<header class="nav">
  <div class="abs brand" style="left:88px;top:18px;font-size:26px">PennaWave</div>
  <a href="#" style="left:482px;color:var(--navy);font-weight:600">Home</a>
  <span class="abs" style="left:497px;top:46px;width:7px;height:7px;border-radius:50%;background:var(--navy)"></span>
  <a href="#" style="left:538px">About</a>
  <a href="#" style="left:593px">Plan &amp; Pricing</a>
  <a href="#" style="left:695px">Testimonial</a>
  <a href="#" style="left:785px">Contact</a>
  <svg class="abs" style="left:886px;top:27px" width="12" height="13" viewBox="0 0 12 13"><circle cx="6" cy="3.5" r="3.2" fill="#1d1d1f"/><path d="M0 13c0-4 2.7-5.5 6-5.5S12 9 12 13z" fill="#1d1d1f"/></svg>
  <a href="#" style="left:910px;font-weight:600">Login</a>
  <div class="abs" style="left:958px;top:14px;width:151px;height:42px;border-radius:22px;background:var(--grad);color:#fff;font-size:13px;font-weight:600;display:flex;align-items:center;justify-content:center">Register Now</div>
</header>

<!-- Hero -->
<section>
  <h1 class="abs" style="left:91px;top:172px;font-size:56px;line-height:1;font-weight:800;color:var(--blue)">Automate</h1>
  <div class="abs" style="left:91px;top:233px;font-size:48px;line-height:1.15;font-weight:600">Your Blog Posting<br>with AI</div>
  <p class="abs" style="left:91px;top:357px;width:434px;font-size:12.5px;line-height:1.6;color:#444">Boost your SEO effortlessly by consistently publishing fresh, keyword-targeted content. Let AI handle your blog, so you can focus on growing your business.</p>
  <div class="btn" style="left:91px;top:434px;width:213px">Start Your Free Trial<span class="arr"><svg width="12" height="12" viewBox="0 0 12 12"><path d="M2 10L10 2M4 2h6v6" stroke="#fff" stroke-width="1.6" fill="none"/></svg></span></div>

  <div class="abs" style="left:91px;top:517px;width:221px;height:77px;background:#fff;border-radius:12px;box-shadow:var(--shadow)">
    <div class="abs" style="left:24px;top:16px;font-size:44px;font-weight:600;line-height:1">4.7</div>
    <div class="abs stars" style="left:102px;top:12px;font-size:13px">★★★★★</div>
    <div class="abs" style="left:102px;top:31px;font-size:11px;color:#444;line-height:1.5">1,938 Rating<br>Searchly Review</div>
  </div>

  <!-- hero visuals -->
  <div class="ph" role="img" aria-label="Decorative soft blue shape behind the hero photos" style="left:660px;top:330px;width:420px;height:310px;border-radius:60% 40% 50% 50%;background:linear-gradient(135deg,#E9F6FB,#7BADD7);opacity:.7"></div>
  <div class="ph" role="img" aria-label="Photo of a smiling woman in a yellow shirt holding a phone and coffee cup" style="left:590px;top:248px;width:240px;height:330px;border-radius:120px 120px 30px 30px;background:linear-gradient(160deg,#6FCCEA 0%,#F2C230 55%,#E5A91C 100%)"></div>
  <div class="ph" role="img" aria-label="Photo of a man sitting cross-legged working on a laptop" style="left:868px;top:108px;width:228px;height:318px;border-radius:24px;background:linear-gradient(180deg,#00A9DD,#0677BA)"></div>
  <span class="abs" style="left:767px;top:120px;width:38px;height:38px;border-radius:9px;background:var(--blue)"></span>
  <span class="abs" style="left:578px;top:408px;width:38px;height:38px;border-radius:9px;background:var(--cyan)"></span>
  <span class="abs" style="left:1040px;top:218px;width:30px;height:30px;border-radius:7px;background:var(--sky)"></span>
  <span class="abs" style="left:518px;top:563px;width:38px;height:38px;border-radius:50%;background:var(--sky)"></span>
  <span class="abs" style="left:882px;top:467px;width:32px;height:32px;border-radius:50%;background:var(--blue);border:3px solid #fff"></span>
  <span class="abs" style="left:1121px;top:150px;width:24px;height:24px;border-radius:50%;background:#E63946"></span>
  <span class="abs" style="left:423px;top:157px;width:14px;height:14px;border-radius:4px;background:#E64A6A;transform:rotate(20deg)"></span>
  <span class="abs" style="left:16px;top:288px;width:50px;height:50px;border-radius:12px;background:var(--ice);transform:rotate(45deg)"></span>
  <div class="abs" style="left:910px;top:493px;width:115px;height:114px;background:#fff;border-radius:26px;box-shadow:var(--shadow);text-align:center">
    <span class="ph" role="img" aria-label="Award medal" style="left:41px;top:16px;width:34px;height:40px;border-radius:50%;background:linear-gradient(#F5C542,#8E5BD8)"></span>
    <div class="abs" style="left:0;top:67px;width:115px;font-size:10px;font-weight:600;color:var(--navy);line-height:1.3">Best Wining<br>Award</div>
  </div>
</section>

<!-- How it works -->
<section>
  <div class="eyebrow" style="top:701px">How It Works</div>
  <h2 class="h2" style="top:731px">Get Started in 3 Easy Steps</h2>

  <div class="step-card" style="left:205px">
    <div class="ico" role="img" aria-label="Blog writing illustration" style="background:linear-gradient(135deg,#C7EBF8,#0677BA)"></div>
    <h3>Create Your Blog</h3>
    <p>Sign up and choose your blog's name, topics, and keywords.</p>
    <span class="go"><svg width="12" height="12" viewBox="0 0 12 12"><path d="M2 10L10 2M4 2h6v6" stroke="#fff" stroke-width="1.6" fill="none"/></svg></span>
  </div>
  <div class="step-card" style="left:477px">
    <div class="ico" role="img" aria-label="Design tools illustration" style="background:linear-gradient(135deg,#6FCCEA,#F2C230);border-radius:50%;width:58px"></div>
    <h3>Customize Your Design</h3>
    <p>Pick a theme, upload your logo, and personalize your color scheme.</p>
    <span class="go"><svg width="12" height="12" viewBox="0 0 12 12"><path d="M2 10L10 2M4 2h6v6" stroke="#fff" stroke-width="1.6" fill="none"/></svg></span>
  </div>
  <div class="step-card" style="left:749px">
    <div class="ico" role="img" aria-label="Blog launch megaphone illustration" style="background:linear-gradient(135deg,#7BADD7,#E63946)"></div>
    <h3>Start Blogging</h3>
    <p>Publish your first post and watch your online presence grow!</p>
    <span class="go"><svg width="12" height="12" viewBox="0 0 12 12"><path d="M2 10L10 2M4 2h6v6" stroke="#fff" stroke-width="1.6" fill="none"/></svg></span>
  </div>

  <div class="btn" style="left:486px;top:1087px;width:225px">Start Blogging Today<span class="arr"><svg width="12" height="12" viewBox="0 0 12 12"><path d="M2 10L10 2M4 2h6v6" stroke="#fff" stroke-width="1.6" fill="none"/></svg></span></div>
</section>

<!-- Why blogging -->
<section>
  <div class="ph" role="img" aria-label="Illustration of two people presenting blog statistics on a large tablet" style="left:93px;top:1173px;width:494px;height:448px;border-radius:40px;background:linear-gradient(135deg,#E9F6FB 0%,#C7EBF8 50%,#7BADD7 100%)"></div>
  <h2 class="abs" style="left:644px;top:1214px;font-size:36px;line-height:1.25;font-weight:600">Why Blogging Matters<br>for Your Business</h2>
  <p class="abs" style="left:644px;top:1322px;width:432px;font-size:12px;line-height:1.9;color:#555">Blogging is more than just sharing ideas—it's a powerful tool to boost your online visibility, establish authority in your niche, and connect with your audience. Consistent blogging drives organic traffic, enhances SEO, and converts visitors into loyal customers.</p>
  <ul class="abs bullets" style="left:644px;top:1427px">
    <li>Boosts Search Engine Rankings.</li>
    <li>Builds Authority &amp; Trust.</li>
    <li>Engages &amp; Grows Your Audience.</li>
    <li>Drives Leads &amp; Sales.</li>
  </ul>
  <div class="btn" style="left:644px;top:1544px;width:291px">Learn More About Our Platform<span class="arr"><svg width="12" height="12" viewBox="0 0 12 12"><path d="M2 10L10 2M4 2h6v6" stroke="#fff" stroke-width="1.6" fill="none"/></svg></span></div>
</section>

<!-- Setup steps -->
<section>
  <div class="setup-band"></div>
  <h2 class="h2" style="top:1794px">4 Simple Steps to Set Up Your Auto Blog</h2>

  <svg class="abs" style="left:444px;top:1990px" width="300" height="180" viewBox="0 0 300 180">
    <path d="M25 172A125 125 0 0 1 61.6 83.6" stroke="#6FCCEA" stroke-width="44" fill="none"/>
    <path d="M61.6 83.6A125 125 0 0 1 150 47" stroke="#0054AA" stroke-width="44" fill="none"/>
    <path d="M150 47A125 125 0 0 1 238.4 83.6" stroke="#0677BA" stroke-width="44" fill="none"/>
    <path d="M238.4 83.6A125 125 0 0 1 275 172" stroke="#0054AA" stroke-width="44" fill="none"/>
    <g fill="#fff" font-family="Poppins, sans-serif" font-size="16" font-weight="600" text-anchor="middle">
      <text x="34" y="130">1</text><text x="102" y="62">2</text><text x="198" y="62">3</text><text x="266" y="130">4</text>
    </g>
    <text x="146" y="133" text-anchor="middle" font-family="Poppins, sans-serif" font-size="27" font-weight="600" fill="#0677BA">PennaWave</text>
  </svg>

  <div class="bubble" style="left:437px;top:1883px"><span class="ico" role="img" aria-label="Blog writing icon" style="background:linear-gradient(135deg,#C7EBF8,#0677BA)"></span></div>
  <div class="bubble" style="left:631px;top:1883px"><span class="ico" role="img" aria-label="New topic ideas icon" style="background:linear-gradient(135deg,#F2C230,#E63946)"></span></div>
  <div class="bubble" style="left:319px;top:2007px"><span class="ico" role="img" aria-label="Scheduling calendar icon" style="background:linear-gradient(135deg,#6FCCEA,#0054AA)"></span></div>
  <div class="bubble" style="left:749px;top:2007px"><span class="ico" role="img" aria-label="Automated blog page icon" style="background:linear-gradient(135deg,#7BADD7,#0054AA)"></span></div>

  <div class="abs setup-txt" style="left:190px;top:1910px;width:220px;text-align:right"><h4>Name Your Blog</h4><p>Choose whether you want daily, weekly, or monthly posts.</p></div>
  <div class="abs setup-txt" style="left:777px;top:1910px;width:270px"><h4>Select Your Blog Topics</h4><p>Pick the topics you want to focus on, or let AI choose them for you.</p></div>
  <div class="abs setup-txt" style="left:90px;top:2048px;width:210px;text-align:right"><h4>Select Frequency</h4><p>Choose whether you want daily, weekly, or monthly posts.</p></div>
  <div class="abs setup-txt" style="left:897px;top:2044px;width:200px"><h4>Go Do Something Else</h4><p>Sit back and let AI do all your blogging, while you focus on what matters</p></div>
</section>

<!-- Pricing -->
<section>
  <div class="eyebrow" style="top:2333px">Plans &amp; Pricing</div>
  <h2 class="h2" style="top:2361px">Choose the Perfect Plan for Your Needs</h2>

  <div class="plan" style="left:178px;width:271px">
    <h3>Base Plan</h3>
    <p class="sm" style="margin:22px 0 16px">1 blog post</p><div class="rule"></div>
    <p class="big">(up to 2,000 words)</p><div class="rule"></div>
    <p class="sm" style="margin-top:26px">every month</p>
    <p class="price">$9.99/mo.</p>
    <div class="cta">Get Started</div>
  </div>
  <div class="plan featured" style="left:463px;width:274px">
    <h3>Premium Plan</h3>
    <p class="sm" style="margin:22px 0 16px">1 blog post</p><div class="rule"></div>
    <p class="big">(up to 3,000 words)</p><div class="rule"></div>
    <p class="sm" style="margin-top:24px;line-height:1.4">per day plus unlimited<br>manual posting</p>
    <p class="price" style="margin-top:20px">$24.99/mo.</p>
    <div class="cta">Get Started</div>
  </div>
  <div class="plan" style="left:755px;width:272px">
    <h3>Ultimate Plan</h3>
    <p class="sm" style="margin:22px 0 16px">1 blog post</p><div class="rule"></div>
    <p class="big">(up to 2,000 words)</p><div class="rule"></div>
    <p class="sm" style="margin-top:32px">every month</p>
    <p class="price" style="margin-top:28px">$14.99/mo.</p>
    <div class="cta">Get Started</div>
  </div>
</section>

<!-- Testimonials -->
<section>
  <div class="eyebrow" style="top:3017px">Testimonials</div>
  <h2 class="h2" style="top:3038px">What Our Users Say</h2>
  <div class="slider-arrow" style="left:992px"><svg width="12" height="14" viewBox="0 0 12 14"><path d="M9 1L3 7l6 6" stroke="#333" stroke-width="1.8" fill="none"/></svg></div>
  <div class="slider-arrow" style="left:1048px"><svg width="12" height="14" viewBox="0 0 12 14"><path d="M3 1l6 6-6 6" stroke="#333" stroke-width="1.8" fill="none"/></svg></div>

  <div class="quote-card" style="left:105px">
    <div class="abs" style="left:34px;top:42px"><div class="stars">★★★★★</div>
      <p>Lorem Ipsum is simply dummy text of the printing and typesetting industry. Lorem Ipsum has been the industry's standard.</p></div>
    <div class="line"></div><div class="who">User A</div>
    <div class="photo" role="img" aria-label="Portrait photo of User A" style="background:linear-gradient(160deg,#C7EBF8,#7BADD7)"></div>
    <div class="qmark">”</div>
  </div>
  <div class="quote-card" style="left:610px">
    <div class="abs" style="left:36px;top:42px"><div class="stars">★★★★★</div>
      <p>Lorem Ipsum is simply dummy text of the printing and typesetting industry. Lorem Ipsum has been the industry's standard.</p></div>
    <div class="line" style="left:36px"></div><div class="who" style="left:36px">User B</div>
    <div class="photo" role="img" aria-label="Portrait photo of User B" style="left:282px;background:linear-gradient(160deg,#C7EBF8,#0677BA)"></div>
    <div class="qmark" style="left:385px">”</div>
  </div>

  <div class="btn" style="left:486px;top:3409px;width:225px">Join Our Community<span class="arr"><svg width="12" height="12" viewBox="0 0 12 12"><path d="M2 10L10 2M4 2h6v6" stroke="#fff" stroke-width="1.6" fill="none"/></svg></span></div>
</section>

<!-- Footer -->
<footer>
  <div class="footer"></div>
  <div class="cta-banner">
    <h2 style="font-size:36px;font-weight:600;margin-top:50px">Ready to Transform Your Blog?</h2>
    <p style="font-size:12px;margin-top:6px">Sign up today and start your free trial. No credit card required!</p>
    <div class="btn light" style="left:289px;top:142px;width:223px">Start Your Free Trial<span class="arr"><svg width="12" height="12" viewBox="0 0 12 12"><path d="M2 10L10 2M4 2h6v6" stroke="#fff" stroke-width="1.6" fill="none"/></svg></span></div>
  </div>
  <div class="abs" style="left:88px;top:3828px;font-size:44px;font-weight:600;color:#fff">PennaWave</div>
  <nav class="foot-links">
    <a href="#" style="left:435px">Home</a>
    <a href="#" style="left:526px">About</a>
    <a href="#" style="left:619px">Plan &amp; Pricing</a>
    <a href="#" style="left:765px">Testimonial</a>
    <a href="#" style="left:897px">Contact</a>
    <a href="#" style="left:1004px">Login/Register</a>
  </nav>
  <div class="abs" style="left:88px;top:3917px;width:1024px;height:1px;background:#555"></div>
  <div class="abs" style="left:0;top:3937px;width:1200px;text-align:center;font-size:13px;color:#fff">© 2024 PennaWave. All rights reserved.</div>
  <div class="abs" style="left:1124px;top:3892px;width:50px;height:50px;border-radius:50%;background:var(--grad);display:flex;align-items:center;justify-content:center">
    <svg width="14" height="18" viewBox="0 0 14 18"><path d="M7 17V2M1 8l6-6 6 6" stroke="#fff" stroke-width="1.8" fill="none"/></svg>
  </div>
</footer>

</body>
</html>
```